Mobile app for deals

Mobile App Name: Vanta 6 Mirk

Design screen shots for the issue of quotes for deals.

1. Loading screen
2. User signs in with credentials or signs up
2. Search by category
3. Search by location
4. Create a project

The expected experience after a project is placed:
- Project alerted
- Quotes
- Project complete
- Rating
- Payment

#TotallyExcited
Updates

Project Deadline Extended Reason: Deadline has been extended on request from a few designers who saw the project late and who would like to submit designs.Thank you to all who submitted on time, we are reviewing your designs and will respond shortly. Added Monday, June 29, 2015

Target Market(s)

Contractors market

Industry/Entity Type

Business Directory

Font styles to use
Sans Serif

Requirements
Must have
• Simple design
• User friendly
• Translateable (later)

```html
<!DOCTYPE html>
<html lang="en">
<head>
<meta charset="utf-8">
<title>Vanta 6 Mirk – App Screens</title>
<link rel="stylesheet" href="https://fonts.googleapis.com/css2?family=Nunito+Sans:wght@400;600;700&display=swap">
<style>
:root{
  --stage:#000000;
  --screen-bg:#f1f1f1;
  --bar-bg:#f7f7f7;
  --row-bg:#ffffff;
  --divider:#dcdcdc;
  --section-bg:#ececec;
  --ink:#1c1c1c;
  --ink-soft:#3a3a3a;
  --muted:#a9a9a9;
  --ios-blue:#1a8cf0;
  --brand-blue:#0f5c99;
  --title-blue:#1a5b96;
  --thumb:#0b3c5a;
  --charcoal:#434343;
  --cancel:#f0553a;
}
*{box-sizing:border-box;margin:0;padding:0}
html,body{width:1200px;height:892px;overflow:hidden;background:var(--stage)}
body{font-family:"Nunito Sans",Helvetica,Arial,sans-serif;color:var(--ink)}
.stage{position:relative;width:1211px;height:900px;transform:scale(0.99092);transform-origin:0 0}
.screen{position:absolute;top:102px;height:648px;background:var(--screen-bg);overflow:hidden}
.screen--welcome{left:0;width:384px}
.screen--projects{left:408px;width:402px}
.screen--account{left:834px;width:377px}

.status-bar{height:20px;background:var(--bar-bg);display:flex;align-items:center;justify-content:space-between;padding:0 8px;font-size:12px;font-weight:600}
.status-bar .signal{display:flex;align-items:center;gap:3px}
.status-bar .battery{display:flex;align-items:center;gap:3px}
.nav-bar{height:44px;background:var(--bar-bg);border-bottom:1px solid var(--divider);position:relative;display:flex;align-items:center;justify-content:center}
.nav-title{font-size:17px;font-weight:600;color:var(--ink)}
.nav-action{position:absolute;top:50%;transform:translateY(-50%);font-size:17px;color:var(--ios-blue)}
.nav-action--right{right:13px}
.nav-action--left{left:8px}
.nav-action--cancel{color:var(--cancel)}
.nav-menu{position:absolute;left:12px;top:12px}

/* Welcome */
.brand{position:absolute;left:0;right:0;top:158px;display:flex;flex-direction:column;align-items:center}
.brand-mark{width:104px;height:104px;border-radius:50%;background:var(--brand-blue)}
.brand-name{margin-top:44px;font-size:23px;font-weight:600;color:var(--brand-blue)}
.welcome-prompt{position:absolute;left:0;right:0;text-align:center;font-size:14px;color:var(--ink-soft);font-weight:600}
.welcome-prompt--pro{top:451px}
.welcome-prompt--client{top:554px;color:var(--brand-blue)}
.cta{position:absolute;left:14px;width:357px;height:42px;border-radius:3px;color:#fff;font-size:17px;font-weight:600;display:flex;align-items:center;justify-content:center}
.cta--pro{top:491px;background:var(--brand-blue)}
.cta--client{top:595px;background:var(--charcoal)}

/* Projects */
.search-band{height:40px;background:var(--section-bg);padding:6px 8px}
.search-field{height:26px;background:#fff;border-radius:5px;display:flex;align-items:center;justify-content:center;gap:6px;color:var(--muted);font-size:14px}
.section-label{height:26px;background:var(--section-bg);font-size:14px;color:var(--ink-soft);padding:4px 16px}
.project-list{list-style:none}
.project-row{height:93px;background:var(--row-bg);border-bottom:1px solid var(--divider);display:flex;align-items:center;padding-left:8px;position:relative}
.project-thumb{width:90px;height:82px;background:var(--thumb);flex:none}
.project-info{margin-left:11px;width:210px;align-self:flex-start;padding-top:9px}
.project-title{font-size:19px;font-weight:700;color:var(--title-blue);line-height:24px}
.project-type{font-size:12px;color:var(--muted);line-height:15px}
.project-desc{font-size:14px;color:var(--ink-soft);line-height:15px;margin-top:5px}
.chevron{position:absolute;right:14px;top:50%;transform:translateY(-50%)}

/* Account */
.form-section{height:34px;background:var(--section-bg);font-size:14px;color:var(--ink-soft);padding:7px 15px}
.form-list{list-style:none;background:var(--row-bg);padding-left:54px}
.form-field{height:42.7px;border-bottom:1px solid var(--divider);display:flex;align-items:center;font-size:16px;color:var(--muted)}
.form-field:last-child{border-bottom:none}
</style>
</head>
<body>
<main class="stage">

  <section class="screen screen--welcome" aria-label="Welcome screen">
    <div class="status-bar">
      <span class="signal"><svg width="34" height="6" viewBox="0 0 34 6"><g fill="#1c1c1c"><circle cx="3" cy="3" r="2.6"/><circle cx="10" cy="3" r="2.6"/><circle cx="17" cy="3" r="2.6"/><circle cx="24" cy="3" r="2.6"/><circle cx="31" cy="3" r="2.6"/></g></svg><svg width="12" height="9" viewBox="0 0 12 9"><path d="M6 9 0.5 3.2a8 8 0 0 1 11 0Z" fill="#1c1c1c"/></svg></span>
      <span>9:41 PM</span>
      <span class="battery">✱100% <svg width="24" height="11" viewBox="0 0 24 11"><rect x="0.5" y="0.5" width="21" height="10" rx="2" fill="none" stroke="#1c1c1c"/><rect x="2" y="2" width="18" height="7" fill="#1c1c1c"/><rect x="22" y="3.5" width="1.6" height="4" fill="#1c1c1c"/></svg></span>
    </div>
    <header class="nav-bar">
      <h1 class="nav-title">Welcome</h1>
      <span class="nav-action nav-action--right">Sign In</span>
    </header>
    <div class="brand">
      <span class="brand-mark"></span>
      <span class="brand-name">Vanta 6 Mirk</span>
    </div>
    <p class="welcome-prompt welcome-prompt--pro">Are you a professional looking for work?</p>
    <span class="cta cta--pro">Get Started!</span>
    <p class="welcome-prompt welcome-prompt--client">Do you have work that needs to be done?</p>
    <span class="cta cta--client">Get Started!</span>
  </section>

  <section class="screen screen--projects" aria-label="Projects screen">
    <div class="status-bar">
      <span class="signal"><svg width="34" height="6" viewBox="0 0 34 6"><g fill="#1c1c1c"><circle cx="3" cy="3" r="2.6"/><circle cx="10" cy="3" r="2.6"/><circle cx="17" cy="3" r="2.6"/><circle cx="24" cy="3" r="2.6"/><circle cx="31" cy="3" r="2.6"/></g></svg><svg width="12" height="9" viewBox="0 0 12 9"><path d="M6 9 0.5 3.2a8 8 0 0 1 11 0Z" fill="#1c1c1c"/></svg></span>
      <span>9:41 PM</span>
      <span class="battery">✱100% <svg width="24" height="11" viewBox="0 0 24 11"><rect x="0.5" y="0.5" width="21" height="10" rx="2" fill="none" stroke="#1c1c1c"/><rect x="2" y="2" width="18" height="7" fill="#1c1c1c"/><rect x="22" y="3.5" width="1.6" height="4" fill="#1c1c1c"/></svg></span>
    </div>
    <header class="nav-bar">
      <svg class="nav-menu" width="26" height="18" viewBox="0 0 26 18"><g stroke="#1a8cf0" stroke-width="1.6"><line x1="0" y1="1" x2="26" y2="1"/><line x1="0" y1="9" x2="26" y2="9"/><line x1="0" y1="17" x2="26" y2="17"/></g></svg>
      <h1 class="nav-title">Projects</h1>
      <span class="nav-action nav-action--right">Add</span>
    </header>
    <div class="search-band">
      <div class="search-field"><svg width="13" height="13" viewBox="0 0 13 13"><circle cx="5.2" cy="5.2" r="4.3" fill="none" stroke="#a9a9a9" stroke-width="1.4"/><line x1="8.4" y1="8.4" x2="12.3" y2="12.3" stroke="#a9a9a9" stroke-width="1.4"/></svg>Search</div>
    </div>
    <div class="section-label">Recent Projects</div>
    <ul class="project-list">
      <li class="project-row"><span class="project-thumb"></span><div class="project-info"><p class="project-title">Project Title</p><p class="project-type">Project type</p><p class="project-desc">Project short description or tags or anything</p></div><svg class="chevron" width="10" height="18" viewBox="0 0 10 18"><path d="M1 1l8 8-8 8" fill="none" stroke="#9a9a9a" stroke-width="2"/></svg></li>
      <li class="project-row"><span class="project-thumb"></span><div class="project-info"><p class="project-title">Project Title</p><p class="project-type">Project type</p><p class="project-desc">Project short description or tags or anything</p></div><svg class="chevron" width="10" height="18" viewBox="0 0 10 18"><path d="M1 1l8 8-8 8" fill="none" stroke="#9a9a9a" stroke-width="2"/></svg></li>
      <li class="project-row"><span class="project-thumb"></span><div class="project-info"><p class="project-title">Project Title</p><p class="project-type">Project type</p><p class="project-desc">Project short description or tags or anything</p></div><svg class="chevron" width="10" height="18" viewBox="0 0 10 18"><path d="M1 1l8 8-8 8" fill="none" stroke="#9a9a9a" stroke-width="2"/></svg></li>
      <li class="project-row"><span class="project-thumb"></span><div class="project-info"><p class="project-title">Project Title</p><p class="project-type">Project type</p><p class="project-desc">Project short description or tags or anything</p></div><svg class="chevron" width="10" height="18" viewBox="0 0 10 18"><path d="M1 1l8 8-8 8" fill="none" stroke="#9a9a9a" stroke-width="2"/></svg></li>
      <li class="project-row"><span class="project-thumb"></span><div class="project-info"><p class="project-title">Project Title</p><p class="project-type">Project type</p><p class="project-desc">Project short description or tags or anything</p></div><svg class="chevron" width="10" height="18" viewBox="0 0 10 18"><path d="M1 1l8 8-8 8" fill="none" stroke="#9a9a9a" stroke-width="2"/></svg></li>
      <li class="project-row"><span class="project-thumb"></span><div class="project-info"><p class="project-title">Project Title</p><p class="project-type">Project type</p><p class="project-desc">Project short description or tags or anything</p></div><svg class="chevron" width="10" height="18" viewBox="0 0 10 18"><path d="M1 1l8 8-8 8" fill="none" stroke="#9a9a9a" stroke-width="2"/></svg></li>
    </ul>
  </section>

  <section class="screen screen--account" aria-label="Account screen">
    <div class="status-bar">
      <span class="signal"><svg width="34" height="6" viewBox="0 0 34 6"><g fill="#1c1c1c"><circle cx="3" cy="3" r="2.6"/><circle cx="10" cy="3" r="2.6"/><circle cx="17" cy="3" r="2.6"/><circle cx="24" cy="3" r="2.6"/><circle cx="31" cy="3" r="2.6"/></g></svg><svg width="12" height="9" viewBox="0 0 12 9"><path d="M6 9 0.5 3.2a8 8 0 0 1 11 0Z" fill="#1c1c1c"/></svg></span>
      <span>9:41 PM</span>
      <span class="battery">✱100% <svg width="24" height="11" viewBox="0 0 24 11"><rect x="0.5" y="0.5" width="21" height="10" rx="2" fill="none" stroke="#1c1c1c"/><rect x="2" y="2" width="18" height="7" fill="#1c1c1c"/><rect x="22" y="3.5" width="1.6" height="4" fill="#1c1c1c"/></svg></span>
    </div>
    <header class="nav-bar">
      <span class="nav-action nav-action--left nav-action--cancel">Cancel</span>
      <h1 class="nav-title">Account</h1>
      <span class="nav-action nav-action--right">Continue</span>
    </header>
    <div class="form-section">Company</div>
    <ul class="form-list">
      <li class="form-field">Name</li>
      <li class="form-field">Industry</li>
      <li class="form-field">Interest</li>
      <li class="form-field">Average Rating</li>
      <li class="form-field">Years of Experience</li>
      <li class="form-field">Number of Projects</li>
      <li class="form-field">Location</li>
      <li class="form-field">Your Business Info</li>
      <li class="form-field">Services Offered</li>
      <li class="form-field">Portfolio</li>
      <li class="form-field">Contact Person</li>
      <li class="form-field">Contact Details</li>
    </ul>
  </section>

</main>
</body>
</html>
```